Business Card Design

we need a bussiness card for the transport company called Varlen Transport
name of contact person that should display on card is Marek Tolleson contact no 0481620357
we do the dry goods and frozen deliveries in melbourne every day
happy to beat any quote

Industry/Entity Type

Business

Contact Information for Business Card

Varlen transport
Marek tolleson
mob 0481620357
contact us for any refrigerator or dry goods delivery
deliver all over melbourne

```html
<!DOCTYPE html>
<html lang="en">
<head>
<meta charset="utf-8">
<title>Varlen Transport – Business Card</title>
<link rel="stylesheet" href="https://fonts.googleapis.com/css2?family=Arimo:wght@400;700&family=Noto+Sans:wght@700;800&display=swap">
<style>
  :root {
    --page-bg: #e9e7e3;
    --card-bg: #f1f1f1;
    --card-edge: #d6d6d6;
    --brand-red: #b8291f;
    --ink: #1d1d1d;
  }
  * { margin: 0; padding: 0; box-sizing: border-box; }
  html, body {
    width: 1200px; height: 1000px; overflow: hidden;
    background: var(--page-bg);
  }
  .canvas { position: relative; width: 1200px; height: 1000px; }
  .card {
    position: absolute; left: 250px; width: 700px; height: 400px;
    background: var(--card-bg);
    border: 1px solid var(--card-edge);
    box-shadow: 0 6px 18px rgba(0,0,0,0.12);
    overflow: hidden;
  }
  .card--front { top: 70px; }
  .card--back { top: 530px; }

  /* Front: text set vertically, reading bottom to top */
  .front__columns {
    position: absolute; left: 250px; bottom: 40px;
    display: flex; align-items: flex-end; gap: 14px;
  }
  .vline {
    writing-mode: vertical-rl;
    transform: rotate(180deg);
    white-space: nowrap;
    line-height: 1;
  }
  .front__mark {
    position: absolute; left: 140px; bottom: 44px;
    width: 40px; height: 40px; border-radius: 50%;
    background: var(--brand-red);
  }
  .front__brand-name {
    font-family: "Arimo", Arial, sans-serif; font-weight: 400;
    font-size: 60px; color: var(--brand-red); letter-spacing: 1px;
  }
  .front__brand-sub {
    font-family: "Arimo", Arial, sans-serif; font-weight: 400;
    font-size: 40px; color: var(--brand-red); letter-spacing: 1px;
    margin-right: 26px;
  }
  .front__name {
    font-family: "Noto Sans", Verdana, sans-serif; font-weight: 800;
    font-size: 52px; color: var(--ink);
  }
  .front__name .initial { color: var(--brand-red); }
  .front__phone {
    font-family: "Noto Sans", Verdana, sans-serif; font-weight: 700;
    font-size: 36px; color: var(--brand-red); letter-spacing: 1px;
    margin-left: 14px;
  }

  /* Back */
  .back__brand {
    position: absolute; left: 330px; top: 52px;
    display: flex; align-items: center; gap: 14px;
    font-family: "Arimo", Arial, sans-serif; color: var(--brand-red);
  }
  .back__brand-mark { width: 20px; height: 20px; border-radius: 50%; background: var(--brand-red); }
  .back__brand-name { font-size: 34px; line-height: 1.05; }
  .back__details {
    position: absolute; left: 50px; top: 150px;
    font-family: "Noto Sans", Verdana, sans-serif; color: var(--ink); font-weight: 700;
  }
  .back__person { font-size: 27px; letter-spacing: 1.5px; }
  .back__area { margin-top: 14px; font-size: 32px; font-weight: 800; letter-spacing: 1.5px; }
  .back__note { margin-top: 26px; font-size: 19px; letter-spacing: 1px; }
</style>
</head>
<body>
<main class="canvas">
  <section class="card card--front" aria-label="Business card front">
    <span class="front__mark"></span>
    <div class="front__columns">
      <span class="vline front__brand-name">VARLEN</span>
      <span class="vline front__brand-sub">TRANSPORT</span>
      <span class="vline front__name">Marek</span>
      <span class="vline front__name"><span class="initial">T</span>olleson</span>
      <span class="vline front__phone">0481620357</span>
    </div>
  </section>

  <section class="card card--back" aria-label="Business card back">
    <div class="back__brand">
      <span class="back__brand-mark"></span>
      <span class="back__brand-name">VARLEN TRANSPORT</span>
    </div>
    <div class="back__details">
      <p class="back__person">Marek Tolleson&nbsp;&nbsp; mob 0481620357</p>
      <p class="back__area">DELIVER ALL OVER MELBOURNE</p>
      <p class="back__note">Contact us for any refrigerator or dry goods delivery</p>
    </div>
  </section>
</main>
</body>
</html>
```